sydney wedding photography business needs a business card design

we need a business card design for a sydney based wedding photography and videography business. our business name is :golden hour photography and video. our target clients are 24-35 yrs female. our style is candid, organic, natural, dynamic. we are a team of young photographers and videographers, and help brides to create memories that they will cherish for the rest of their lives. the logo will be provided. we want an elegant design that reflects our style, and also want to give a great impression to our clients that we are one of the best studios in sydney and our brand means quality and premium service.

Target Market(s)

bride to be, 24-35 years old, living in sydney and surrunding areas

Industry/Entity Type

Wedding Photography

Contact Information for Business Card

address: 57 marrow lane, bexton nsw 2041
mobile: 0431872056
phone: (02) 9361 2748
info@goldenhourstudio.net.au
www.goldenhourstudio.net.au
facebook:goldenhourbridals
instagram:goldenhourbridals

Font styles to use
Serif
Sans Serif

Requirements
Nice to have
• maybe add my slogan"memories beyond eternity" if the layout looks good
Should not have
• no black color, not good idea for wedding biz card

```html
<!DOCTYPE html>
<html lang="en">
<head>
<meta charset="utf-8">
<title>Golden Hour Photography – Business Card</title>
<link href="https://fonts.googleapis.com/css2?family=Josefin+Sans:wght@400;600&display=swap" rel="stylesheet">
<style>
  :root {
    --backdrop: #3a3a3a;
    --card: #ffffff;
    --gold: #c08a2e;
    --bronze: #6b4a1e;
    --ink: #3a3530;
    --rule: #5a5550;
    --faint: #ececec;
  }
  * { margin: 0; padding: 0; box-sizing: border-box; }
  html, body { width: 1200px; height: 900px; overflow: hidden; }
  body {
    background: var(--backdrop);
    font-family: "Josefin Sans", sans-serif;
    color: var(--ink);
    position: relative;
  }
  .card {
    position: absolute;
    top: 301px;
    width: 515px;
    height: 297px;
    background: var(--card);
    overflow: hidden;
  }
  .card--front { left: 72px; }
  .card--back { left: 614px; }

  /* front */
  .decor-area {
    position: absolute;
    background: linear-gradient(160deg, #f3f3f3, var(--faint));
  }
  .decor-area--corner { left: 420px; top: 0; width: 95px; height: 95px; }
  .decor-area--base { left: 0; top: 185px; width: 105px; height: 112px; }
  .brand-frame {
    position: absolute;
    left: 101px; top: 106px;
    width: 312px; height: 84px;
    border: 1.5px solid var(--gold);
    text-align: center;
    padding-top: 12px;
  }
  .brand-name {
    font-weight: 600;
    color: var(--gold);
    line-height: 1;
  }
  .brand-name__title { display: block; font-size: 36px; letter-spacing: 0.5px; }
  .brand-name__sub { display: block; font-size: 13px; letter-spacing: 6px; margin-top: 4px; }
  .slogan {
    position: absolute;
    left: 101px; top: 205px;
    width: 330px;
    font-size: 12px;
    letter-spacing: 5.2px;
    color: var(--bronze);
    white-space: nowrap;
  }
  .slogan__accent { color: var(--gold); }

  /* back */
  .brand-box {
    position: absolute;
    left: 34px; top: 28px;
    width: 446px; height: 100px;
    border: 1px solid var(--rule);
    text-align: center;
    padding-top: 20px;
  }
  .brand-box .brand-name__title { font-size: 40px; }
  .brand-box .brand-name__sub { font-size: 14px; letter-spacing: 7px; margin-top: 6px; }
  .services {
    position: absolute;
    left: 34px; top: 143px;
    width: 446px;
    text-align: center;
    font-size: 12px;
    letter-spacing: 5.6px;
    color: var(--ink);
    white-space: nowrap;
  }
  .contact-table {
    position: absolute;
    left: 34px; top: 159px;
    width: 446px; height: 110px;
    border: 1px solid var(--rule);
  }
  .contact-col {
    position: absolute;
    top: 0; height: 82px;
    padding-top: 9px;
    font-size: 12.5px;
    line-height: 17px;
  }
  .contact-col--person { left: 0; width: 223px; padding-left: 30px; border-right: 1px solid var(--rule); }
  .contact-col--place { left: 223px; width: 223px; padding-left: 30px; padding-top: 16px; }
  .contact-line { display: flex; align-items: center; gap: 8px; white-space: nowrap; }
  .contact-line--indent { padding-left: 17px; }
  .contact-line--gap { margin-top: 2px; }
  .icon { width: 10px; height: 10px; flex: none; fill: var(--gold); }
  .social-row {
    position: absolute;
    left: 0; top: 82px;
    width: 100%; height: 27px;
    border-top: 1px solid var(--rule);
    display: flex; justify-content: center; align-items: center; gap: 10px;
    font-size: 12.5px;
  }
  .social-handle { display: flex; align-items: center; gap: 5px; }
  .social-mark { width: 10px; height: 10px; background: var(--gold); border-radius: 2px; }
</style>
</head>
<body>

<section class="card card--front" aria-label="Card front">
  <div class="decor-area decor-area--corner" role="img" aria-label="Faint decorative artwork area"></div>
  <div class="decor-area decor-area--base" role="img" aria-label="Faint decorative artwork area"></div>
  <div class="brand-frame">
    <p class="brand-name">
      <span class="brand-name__title">Golden Hour</span>
      <span class="brand-name__sub">PHOTOGRAPHY</span>
    </p>
  </div>
  <p class="slogan">MEMORIES <span class="slogan__accent">BEYOND ETERNITY</span></p>
</section>

<section class="card card--back" aria-label="Card back">
  <div class="brand-box">
    <p class="brand-name">
      <span class="brand-name__title">Golden Hour</span>
      <span class="brand-name__sub">PHOTOGRAPHY</span>
    </p>
  </div>
  <p class="services">WEDDING | ENGAGEMENT | FAMILY</p>

  <div class="contact-table">
    <div class="contact-col contact-col--person">
      <p class="contact-line">
        <svg class="icon" viewBox="0 0 10 10"><circle cx="5" cy="5" r="5"/><circle cx="5" cy="4" r="1.8" fill="#fff"/><path d="M1.8 8.3a3.5 3.5 0 0 1 6.4 0" fill="#fff"/></svg>
        DANIEL REYES
      </p>
      <p class="contact-line">
        <svg class="icon" viewBox="0 0 10 10"><rect x="2.5" y="0" width="5" height="10" rx="1"/><rect x="3.3" y="1.2" width="3.4" height="6.5" fill="#fff"/></svg>
        0431 872 056
      </p>
      <p class="contact-line">
        <svg class="icon" viewBox="0 0 10 10"><path d="M0 4c0-2 10-2 10 0v1.5H7.3V4H2.7v1.5H0z"/><path d="M2 6h6l1 3H1z"/></svg>
        (02) 9361 2748
      </p>
      <p class="contact-line">
        <svg class="icon" viewBox="0 0 10 10"><rect x="0" y="1.5" width="10" height="7"/><path d="M0.5 2l4.5 3.5L9.5 2" fill="none" stroke="#fff" stroke-width="0.9"/></svg>
        info@goldenhourstudio.net.au
      </p>
    </div>
    <div class="contact-col contact-col--place">
      <p class="contact-line">
        <svg class="icon" viewBox="0 0 10 10"><path d="M5 0a3.6 3.6 0 0 0-3.6 3.6C1.4 6.3 5 10 5 10s3.6-3.7 3.6-6.4A3.6 3.6 0 0 0 5 0z"/><circle cx="5" cy="3.6" r="1.3" fill="#fff"/></svg>
        57 marrow lane
      </p>
      <p class="contact-line contact-line--indent">bexton nsw 2041</p>
      <p class="contact-line contact-line--gap">
        <svg class="icon" viewBox="0 0 10 10"><circle cx="5" cy="5" r="4.5" fill="none" stroke="var(--gold)" stroke-width="1"/><ellipse cx="5" cy="5" rx="2" ry="4.5" fill="none" stroke="var(--gold)" stroke-width="0.8"/><path d="M0.5 5h9" stroke="var(--gold)" stroke-width="0.8"/></svg>
        www.goldenhourstudio.net.au
      </p>
    </div>
    <div class="social-row">
      <span class="social-handle"><span class="social-mark"></span>goldenhourbridals</span>
      <span class="social-handle"><span class="social-mark"></span>goldenhourbridals</span>
    </div>
  </div>
</section>

</body>
</html>
```